Home page web design for "Tales from Tamsin"

We need a home page web design for a start up company that will write memoirs for seniors.
The completed project will need to include PSD files...NO HTML or CSS necessary.
Attached is a brief outline concept that may give you some ideas...but you are the creative professionals, so please feel free to add your ideas. We will also attach some files that show you our logo, brochures, and photos that could be used to give you ideas of our focus.
There will need to be access to the other pages on the home page to include: 'About Us'; 'How We Can Help'; 'Community Sessions'; 'Senior Consulting ' and 'Contact Us'.
Updates

Project Deadline Extended Reason: We want designers to have sufficient time to get all their proposals and revisions submitted. THANK YOU Added Wednesday, October 15, 2014

Target Market(s)

Seniors and Baby Boomers

Industry/Entity Type

It Company

Number of Pages Required

1 page

Colors
f9ba93
fbca95
faa54b
faf289
f37123

Requirements
Must have
• Script easy on senior eyes.
• Initial contact number would be 844-4LEGACY
Nice to have
• While the color pallet is non-specific we prefer the warm colors.
• salmon, peach.......
• NOT so much the orange of Halloween:)
• However, please utilize your creativity and put in colors you feel will draw best with your design.

```html
<!DOCTYPE html>
<html lang="en">
<head>
<meta charset="utf-8">
<title>Tales from Tamsin – Home</title>
<link href="https://fonts.googleapis.com/css2?family=Open+Sans:wght@300;400;600;700&family=Cabin:wght@400;600&family=Kalam:wght@400;700&display=swap" rel="stylesheet">
<style>
  :root {
    --bg-deep: #7a1f12;
    --bg-orange: #e0651c;
    --bg-glow: #f39a3c;
    --ink: #1a1a1a;
    --bar: #151515;
    --cream: #f4efd9;
    --cream-dark: #ebe4c7;
    --gold: #c9962d;
    --gold-dark: #b57f1f;
    --maroon: #4a1a12;
    --maroon-line: #7a2a1b;
    --card: #3e140d;
    --card-dark: #2a0f0b;
    --card-text: #d7c1b4;
    --tan: #dcc8a0;
    --tan-dark: #4a3a28;
    --text: #333;
    --white: #fff;
    --social: #2f5d97;
    --tagline-red: #8a1f12;
    --link: #a0541c;
  }
  * { box-sizing: border-box; margin: 0; padding: 0; }
  html, body { width: 1200px; height: 800px; overflow: hidden; }
  body {
    position: relative;
    font-family: "Open Sans", Arial, sans-serif;
    color: var(--text);
    background: var(--bg-orange);
  }
  .backdrop {
    position: absolute; inset: 0;
    background:
      radial-gradient(ellipse at 85% 35%, rgba(243,154,60,.55), transparent 55%),
      radial-gradient(ellipse at 20% 20%, rgba(150,40,25,.7), transparent 60%),
      linear-gradient(180deg, var(--bg-deep) 0%, #b9401a 45%, var(--bg-orange) 75%, #ea7a2a 100%);
  }
  .top-strip { position: absolute; left: 0; top: 0; width: 1200px; height: 10px; background: var(--bar); }

  .site-header {
    position: absolute; left: 315px; top: 16px; width: 570px; height: 95px;
    background: var(--cream); border-top-right-radius: 28px;
  }
  .brand {
    position: absolute; left: 22px; top: 26px; display: flex; align-items: center; gap: 8px;
    font-family: "Open Sans", sans-serif; font-weight: 600; font-size: 19px; color: var(--gold-dark);
  }
  .brand-mark { width: 14px; height: 14px; border-radius: 50%; background: var(--gold); }
  .tagline {
    position: absolute; left: 226px; top: 45px; width: 244px;
    font-family: "Kalam", cursive; font-size: 10.5px; line-height: 13px;
    color: #2d2a20; white-space: nowrap;
  }
  .tagline em { display: block; font-style: normal; color: var(--tagline-red); text-align: right; padding-right: 18px; }
  .follow {
    position: absolute; right: 0; top: 40px; width: 94px; height: 55px; background: var(--cream-dark);
    text-align: center; font-size: 9px; font-weight: 700; color: var(--ink); padding-top: 6px;
  }
  .follow .icons { display: flex; justify-content: center; gap: 8px; margin-top: 3px; }
  .social-dot { width: 26px; height: 26px; border-radius: 50%; background: var(--social); border: 2px solid #dfe8f4; }

  .main-nav {
    position: absolute; left: 0; top: 111px; width: 1200px; height: 24px; background: var(--bar);
    border-top: 1px solid #333; display: flex; justify-content: center; align-items: center;
  }
  .main-nav a {
    color: var(--white); text-decoration: none; font-size: 10px; font-weight: 600; padding: 0 9px;
    border-left: 1px solid #666; line-height: 10px;
  }
  .main-nav a:first-child { border-left: 0; }

  .hero { position: absolute; left: 315px; top: 135px; width: 570px; height: 175px; border-bottom-left-radius: 22px; overflow: hidden; }
  .hero-panel { position: absolute; left: 0; top: 0; width: 218px; height: 175px; background: linear-gradient(180deg, #cf9a35, #b8832a); }
  .hero-photo {
    position: absolute; left: 218px; top: 0; width: 352px; height: 175px;
    background: radial-gradient(ellipse at 40% 45%, #6b5a4a 0%, #3a3028 40%, #1c1713 100%);
  }
  .hero-caption {
    position: absolute; left: 5px; top: 48px; width: 213px; height: 52px; background: rgba(70,50,30,.78);
    color: var(--white); padding: 4px 0 0 12px;
  }
  .hero-caption .line1 { font-weight: 300; font-size: 22px; line-height: 24px; }
  .hero-caption .line2 { font-weight: 400; font-size: 15px; line-height: 18px; }
  .hero-dots { position: absolute; left: 158px; top: 157px; display: flex; gap: 3px; }
  .hero-dots span { width: 10px; height: 10px; border-radius: 50%; background: #7a5a2a; }
  .hero-dots span.active { background: var(--white); }

  .services {
    position: absolute; left: 315px; top: 319px; width: 570px; height: 103px; background: var(--maroon);
    display: flex; padding: 4px; gap: 4px;
  }
  .service { flex: 1; border: 1px solid var(--maroon-line); padding: 7px 10px; position: relative; background: var(--card); }
  .service.dark { background: var(--card-dark); border-color: #1a0806; }
  .service h3 { color: var(--white); font-size: 11.5px; font-weight: 600; white-space: nowrap; }
  .service .thumb {
    position: absolute; left: 9px; top: 28px; width: 51px; height: 51px; border-radius: 50%;
    background: radial-gradient(circle at 50% 40%, #d9c6b8, #8a6a5a); border: 2px solid #e8dcd0;
  }
  .service p {
    position: absolute; left: 66px; top: 29px; right: 4px;
    font-size: 7px; line-height: 10px; color: var(--card-text);
  }
  .read-more {
    position: absolute; left: 66px; top: 72px; width: 52px; height: 16px; border-radius: 8px; background: var(--gold);
    color: #2a1a0a; font-size: 7px; text-align: center; line-height: 16px;
  }

  .join {
    position: absolute; left: 315px; top: 433px; width: 570px; height: 59px; background: var(--tan);
    border-top: 2px solid #ece0c4;
  }
  .join .photo {
    position: absolute; left: 10px; top: 0; width: 54px; height: 56px; transform: rotate(-8deg);
    background: linear-gradient(135deg, #c9a48a, #7a5a48); border: 3px solid var(--white);
  }
  .join h2 { position: absolute; left: 80px; top: 13px; font-size: 17px; font-weight: 700; color: #3a2818; line-height: 17px; }
  .join h2 small { display: block; font-size: 10px; font-weight: 700; padding-left: 6px; line-height: 12px; }
  .join .divider { position: absolute; left: 254px; top: 10px; width: 1px; height: 38px; background: var(--tan-dark); }
  .field {
    position: absolute; top: 20px; width: 113px; height: 19px; background: var(--white); border: 1px solid #a99; font-size: 7px;
    padding: 4px 5px; color: #333;
  }
  .signup {
    position: absolute; left: 502px; top: 20px; width: 57px; height: 19px; background: linear-gradient(#444, #111);
    color: var(--white); font-size: 9px; font-weight: 700; text-align: center; line-height: 19px; border-radius: 2px;
  }

  .intro {
    position: absolute; left: 315px; top: 506px; width: 570px; height: 204px; background: var(--white);
    padding: 18px 20px; border: 1px solid #ddd;
  }
  .intro h1 { font-family: "Cabin", sans-serif; font-weight: 400; font-size: 19px; color: var(--ink); line-height: 22px; }
  .intro h4 { font-family: "Cabin", sans-serif; font-weight: 600; font-size: 11px; color: var(--ink); margin-bottom: 8px; }
  .intro p {
    font-size: 7.5px; font-weight: 600; color: #3a3a3a; line-height: 10px; width: 416px;
    margin-bottom: 9px; letter-spacing: -0.08px;
  }
  .intro .learn { font-size: 8px; font-weight: 700; color: var(--link); text-decoration: underline; }
  .intro .oval {
    position: absolute; left: 443px; top: 38px; width: 101px; height: 145px; border-radius: 50%;
    background: radial-gradient(ellipse at 50% 45%, #a0704a, #4a2a18); box-shadow: 0 2px 6px rgba(0,0,0,.35);
  }

  .site-footer {
    position: absolute; left: 315px; top: 710px; width: 570px; height: 25px; background: var(--bar);
    border-bottom-left-radius: 18px; color: #ccc; font-size: 6.5px;
  }
  .site-footer .copy { position: absolute; left: 20px; top: 9px; }
  .site-footer .icons { position: absolute; left: 265px; top: 4px; display: flex; gap: 6px; }
  .site-footer .social-dot { width: 16px; height: 16px; border-width: 1px; }
</style>
</head>
<body>
  <div class="backdrop" role="img" aria-label="Warm orange-toned photo of an older man reading, softly blurred"></div>
  <div class="top-strip"></div>

  <header class="site-header">
    <div class="brand"><span class="brand-mark"></span>Tales from Tamsin</div>
    <p class="tagline">Every life legacy is a gift to be treasured by the <em>next generation...</em></p>
    <div class="follow">follow us on
      <div class="icons"><span class="social-dot" aria-label="Social link"></span><span class="social-dot" aria-label="Social link"></span></div>
    </div>
  </header>

  <nav class="main-nav">
    <a href="#">Home</a><a href="#">About Us</a><a href="#">How We Can Help</a><a href="#">Community Services</a><a href="#">Senior Consulting Services</a><a href="#">Contact Us</a>
  </nav>

  <section class="hero">
    <div class="hero-panel"></div>
    <div class="hero-photo" role="img" aria-label="Senior man holding up his printed memoir book"></div>
    <div class="hero-caption"><div class="line1">ORDINARY LIVES</div><div class="line2">EXTRAORDINARY LEGACIES</div></div>
    <div class="hero-dots"><span></span><span class="active"></span><span></span><span></span></div>
  </section>

  <section class="services">
    <article class="service">
      <h3>How We Can Help</h3>
      <div class="thumb" role="img" aria-label="Woman writing at a table"></div>
      <p>Do you know the triumphs and tribulations of your ancestors?</p>
      <span class="read-more">read more</span>
    </article>
    <article class="service dark">
      <h3>Community Services</h3>
      <div class="thumb" role="img" aria-label="Group of young people together"></div>
      <p>A biography can place a deeper relevance on the face for future descendants. Every life is...</p>
      <span class="read-more">read more</span>
    </article>
    <article class="service">
      <h3>Senior Consulting Services</h3>
      <div class="thumb" role="img" aria-label="Smiling senior woman"></div>
      <p>A genealogy, while very relevant, doesn't offer the personal story of the...</p>
      <span class="read-more">read more</span>
    </article>
  </section>

  <section class="join">
    <div class="photo" role="img" aria-label="Snapshot of joined hands"></div>
    <h2>Join the Community<small>Sign up for FREE Consultation</small></h2>
    <div class="divider"></div>
    <div class="field" style="left:266px">Full Name</div>
    <div class="field" style="left:384px">Email Address</div>
    <div class="signup">SIGN UP</div>
  </section>

  <section class="intro">
    <h1>Tales from Tamsin</h1>
    <h4>When a genealogy doesn't say enough!</h4>
    <p>If you were alive in 100 years, what would you share with your descendants?</p>
    <p>Now you have a vehicle to help you immortalize your thoughts for the future..specifically for those who will want to know!</p>
    <p>We are not all presidents of countries or CEO's of fortune 500 companies! But "every life legacy is a gift to be treasured by the next generation."</p>
    <p>Does your family host generations of soldiers, doctors, farmers, scientists, mechanics, entrepreneurs, writers, politicians, contractors, pastors, artisans, athletes, musicians, etc..? Generational patterns can often emerge when</p>
    <a class="learn" href="#">Learn More</a>
    <div class="oval" role="img" aria-label="Senior woman writing at an antique desk"></div>
  </section>

  <footer class="site-footer">
    <span class="copy">Copyright © 2014. All rights Reserved</span>
    <div class="icons"><span class="social-dot"></span><span class="social-dot"></span></div>
  </footer>
</body>
</html>
```